RIPTALON boardgrip need a Packaging Design Boxes for brand new label of wax

You could be the designer of the biggest surfboard wax brand ever.

We need a new packaging design for a new brand based in near Sydney Australia. The Coal Coast. We are called RIPTALON boardgrip. Packaging is to be a Folding box using recycled paper/cardboard. It must hold 100 grams of wax. So the box must be around 8 cms x 8 cms x 3 cms in height.The box blue print lay out is needed for printing.Our surfboard wax comes in 5 scents including Coconut / Lime, Mango, Passionfruit, Bubblegum and Strawberry / Cream. Our scented wax is unique in this industry by our range of scents. And aslo hand made in Australia. The wax comes in 4 water temperatures Tropical, Warm, Cool and Cold. So 5 individual scented boxes with a 4 generic water temperatures temple on each.
The name riptalon refers to the colloquial sporting
term that is used when the rider has successfully completed a maneuver- such as ' he totally riptalon that move'. Although we do link the brand name riptalon to the scents and green initiatives in the making of our product. Also packaging must say things like Made on The Coal Coast NSW Australia, Do not Eat, 100 grams, Hand Made, What scent it is, Store in cool place, template for water temperature and a area for a bar code

Target Market(s)

Surfing, surfer is the target customers age from 10 years and up. Both male and female. This is a very new brand about to hit the east coast of Australia.

Industry/Entity Type

Industry

Requirements
Must have
• The box must hold a round block of surfboard wax. 8 cms in diameter and 2.8 cms in height. Open to printed color or browm box.
Nice to have
• The name RIPTALON boardgrip is the name. Hold fast and ride tall, is the catch phrase.100 grams and a water temperature measurement gauge for the 4 tropical, warm, cool and cold. Which can be used by me marking it when needed.Top of box wax comes in 6 fragrance so will need 1 for each scent .Hand made on the Coal Coast NSW.
Trying for a tuff stance kind of look
Should not have
• This is a surfboard wax not hair wax or anything.
So not girlllly

```html
<!DOCTYPE html>
<html lang="en">
<head>
<meta charset="utf-8">
<title>RIPTALON boardgrip – Coconut // Lime box dieline</title>
<link rel="stylesheet" href="https://fonts.googleapis.com/css2?family=Bree+Serif&family=Oswald:wght@500;600&display=swap">
<style>
  :root {
    --kraft: #cfbfa5;
    --kraft-deep: #bfae92;
    --ray-green: #7cc242;
    --ray-lime: #9bd85a;
    --ink: #2a2a2a;
    --paper: #ffffff;
    --cut-line: #e0218a;
    --fold-line: #e0218a;
    --gauge-1: #4e9a2c;
    --gauge-2: #62b236;
    --gauge-3: #78c943;
    --gauge-4: #92de55;
    --note: #8a8a8a;
  }
  html, body {
    margin: 0;
    padding: 0;
    background: var(--paper);
    overflow: hidden;
  }
  .canvas {
    position: relative;
    width: 1137px;
    height: 1200px;
    overflow: hidden;
    background: var(--paper);
  }
  .spec-note {
    position: absolute;
    left: 30px;
    top: 18px;
    font: 500 14px "Oswald", sans-serif;
    color: var(--note);
    letter-spacing: 0.3px;
  }
  .dieline {
    position: absolute;
    left: 0;
    top: 0;
  }
  .headline {
    font-family: "Bree Serif", serif;
    font-size: 31px;
    fill: var(--ink);
    letter-spacing: 0.5px;
  }
  .brand-name {
    font-family: "Bree Serif", serif;
    font-size: 54px;
    fill: var(--ink);
    letter-spacing: 2px;
  }
  .brand-sub {
    font-family: "Bree Serif", serif;
    font-size: 15px;
    fill: var(--ink);
  }
  .scent-name {
    font-family: "Bree Serif", serif;
    font-size: 29px;
    fill: var(--ink);
    letter-spacing: 0.5px;
  }
  .weight-label {
    font-family: "Bree Serif", serif;
    font-size: 22px;
    fill: var(--ink);
  }
  .side-copy {
    font-family: "Oswald", sans-serif;
    font-weight: 600;
    font-size: 17px;
    fill: var(--ink);
    letter-spacing: 0.3px;
  }
  .band-name {
    font-family: "Bree Serif", serif;
    font-size: 28px;
    fill: var(--kraft);
    letter-spacing: 1px;
  }
  .barcode-hint {
    font-family: "Oswald", sans-serif;
    font-weight: 500;
    font-size: 10px;
    fill: #555;
    letter-spacing: 1px;
  }
  .cut { fill: none; stroke: var(--cut-line); stroke-width: 1.6; }
  .fold { fill: none; stroke: var(--fold-line); stroke-width: 1.2; stroke-dasharray: 3 4; }
</style>
</head>
<body>
<div class="canvas">
  <div class="spec-note">Dimensions: 8 x 8 x 3 cm</div>

  <svg class="dieline" width="1137" height="1200" viewBox="0 0 1137 1200" xmlns="http://www.w3.org/2000/svg">
    <defs>
      <radialGradient id="burst-front" cx="383" cy="440" r="420" gradientUnits="userSpaceOnUse">
        <stop offset="0" stop-color="var(--ray-lime)"/>
        <stop offset="0.35" stop-color="#b5cc88"/>
        <stop offset="1" stop-color="var(--kraft)"/>
      </radialGradient>
      <radialGradient id="burst-base" cx="367" cy="957" r="260" gradientUnits="userSpaceOnUse">
        <stop offset="0" stop-color="var(--ray-green)"/>
        <stop offset="0.45" stop-color="#aecb82"/>
        <stop offset="1" stop-color="var(--kraft)"/>
      </radialGradient>
      <linearGradient id="burst-side-left" x1="1" y1="0.5" x2="0" y2="0.5">
        <stop offset="0" stop-color="#b9cf8c"/>
        <stop offset="1" stop-color="var(--kraft)"/>
      </linearGradient>
      <linearGradient id="burst-side-right" x1="0" y1="0.5" x2="1" y2="0.5">
        <stop offset="0" stop-color="#b9cf8c"/>
        <stop offset="1" stop-color="var(--kraft)"/>
      </linearGradient>
    </defs>

    <!-- Lid tuck flap + front panel -->
    <g class="panel panel-front" role="img" aria-label="Green sunburst rays radiating across the kraft front panel and lid">
      <path d="M198 668 L198 80 L216 58 L551 58 L569 80 L569 668 Z" fill="url(#burst-front)"/>
    </g>

    <!-- Left side panel -->
    <g class="panel panel-side-left" role="img" aria-label="Green sunburst rays on kraft side panel">
      <path d="M198 215 L198 668 L58 668 L58 238 Q58 215 80 215 Z" fill="url(#burst-side-left)"/>
    </g>

    <!-- Right side panel -->
    <g class="panel panel-side-right" role="img" aria-label="Green sunburst rays on kraft side panel">
      <path d="M569 215 L569 668 L710 668 L710 238 Q710 215 688 215 Z" fill="url(#burst-side-right)"/>
    </g>

    <!-- Barcode strip with glue tabs -->
    <g class="panel panel-barcode">
      <path d="M165 655 L198 668 L198 755 L165 765 Z" fill="var(--kraft)"/>
      <path d="M602 655 L569 668 L569 755 L602 765 Z" fill="var(--kraft)"/>
      <rect x="198" y="652" width="371" height="115" fill="var(--kraft)"/>
      <rect x="211" y="652" width="350" height="112" fill="var(--paper)"/>
      <text class="barcode-hint" x="386" y="713" text-anchor="middle">BARCODE AREA</text>
    </g>

    <!-- Base panel -->
    <g class="panel panel-base" role="img" aria-label="Green sunburst rays bursting from the centre of the kraft base panel">
      <path d="M165 767 L569 767 L569 1147 L418 1147 A35 35 0 0 0 348 1147 L165 1147 Z" fill="url(#burst-base)"/>
    </g>

    <!-- Brand band: left diagonal -->
    <polygon class="band band-left" points="198,412 198,495 58,572 58,480" fill="var(--ink)"/>
    <text class="band-name" transform="translate(128 515) rotate(-29)" text-anchor="middle">RIPTALON</text>

    <!-- Brand band: right diagonal with temperature gauge -->
    <polygon class="band band-right" points="569,412 569,495 710,572 710,480" fill="var(--ink)"/>
    <g class="temp-gauge">
      <rect x="586" y="440" width="20" height="30" fill="var(--gauge-1)"/>
      <rect x="614" y="452" width="20" height="32" fill="var(--gauge-2)"/>
      <rect x="642" y="466" width="20" height="33" fill="var(--gauge-3)"/>
      <rect x="670" y="480" width="20" height="34" fill="var(--gauge-4)"/>
    </g>

    <!-- Front panel copy -->
    <text class="headline" x="383" y="362" text-anchor="middle">HOLD FAST AND</text>
    <text class="headline" x="383" y="396" text-anchor="middle">RIDE TALL</text>

    <rect class="brand-box" x="198" y="412" width="371" height="83" fill="var(--kraft)" stroke="var(--ink)" stroke-width="5"/>
    <text class="brand-name" x="383" y="470" text-anchor="middle">RIPTALON</text>
    <text class="brand-sub" x="512" y="488" text-anchor="middle">boardgrip</text>

    <rect class="scent-box" x="198" y="495" width="371" height="52" fill="none" stroke="var(--ink)" stroke-width="5"/>
    <text class="scent-name" x="383" y="532" text-anchor="middle">COCONUT // LIME</text>

    <text class="weight-label" x="383" y="612" text-anchor="middle">100 GRAMS</text>

    <!-- Left side panel copy -->
    <g class="side-copy-group side-copy-left">
      <text class="side-copy" transform="translate(178 236) rotate(90)">DO NOT EAT</text>
      <text class="side-copy" transform="translate(156 236) rotate(90)">STORE IN COOL PLACE</text>
      <text class="side-copy" transform="translate(134 236) rotate(90)">HAND MADE ON THE</text>
      <text class="side-copy" transform="translate(112 236) rotate(90)">COAL COAST NSW AUSTRALIA</text>
    </g>

    <!-- Right side panel temperature labels -->
    <g class="side-copy-group side-copy-right">
      <text class="side-copy" transform="translate(584 340) rotate(90)">TROPICAL</text>
      <text class="side-copy" transform="translate(606 364) rotate(90)">WARM</text>
      <text class="side-copy" transform="translate(628 382) rotate(90)">COOL</text>
      <text class="side-copy" transform="translate(650 398) rotate(90)">COLD</text>
    </g>

    <!-- Cut lines -->
    <path class="cut" d="M198 215 L198 80 L216 58 L551 58 L569 80 L569 215 L688 215 Q710 215 710 238 L710 668 L569 668 L569 767 L569 1147 L418 1147 A35 35 0 0 0 348 1147 L165 1147 L165 767 L198 767 L198 668 L58 668 L58 238 Q58 215 80 215 Z"/>
    <path class="cut" d="M198 668 L165 655 L165 765 L198 767"/>
    <path class="cut" d="M569 668 L602 655 L602 765 L569 767"/>

    <!-- Fold lines -->
    <line class="fold" x1="198" y1="215" x2="569" y2="215"/>
    <line class="fold" x1="198" y1="215" x2="198" y2="668"/>
    <line class="fold" x1="569" y1="215" x2="569" y2="668"/>
    <line class="fold" x1="198" y1="668" x2="569" y2="668"/>
    <line class="fold" x1="198" y1="767" x2="569" y2="767"/>
  </svg>
</div>
</body>
</html>
```